Basic Commercial & Residential Real Estate Web Site

I need a basic website for a new real estate company that deals with both residential and commercial sales. It must be clean and professional. We sell homes, office buildings, farms, and ranches. It should feel crisp and clean.
I need a main page with my logo and links to commercial, residential, farm and land searches with contact data forms. Also incorporated would be a mls property search (IDX) form. I am in Northern California and the current site I posted is at www.tqvandel.com. I need the functionality of the links and the supporting pages. I do not have all the copy ready because I did not know what to expect.
Updates

Project Deadline Extended
Reason: I apologize, I am extremely busy and you all need more data to do a good job. All the designs are great so far and it is extremely difficult to choose at this point. I haven't given you enough data. I haver now uploaded some relevent photos (not very good) and edited the brief. I am looking for what I call the Landing or main page with some functionality built in to other pages which I also need. Example if you click on "Commercial" it should go to a page that discusses our commercial dept.......

I would like to thank all the designers for all their hard work and efforts, I wish I could reward you all.

Thanks again for your creative and professional designs.

Gareth

Target Market(s)

Corporate Execs for the Commercial Buildings
Homeowners/Families for the Homes and Farms
Upper end people for the land to build estates

Industry/Entity Type

Real Estate

Font styles to use
Sans Serif

Requirements
Must have
• Our Logo should be prominent, pronounced
Need contact data or button
Functional Page that links to other data pages
Must Have a "search for properties" feature
Must say "Commercial and Residential Representation"
Pictures of Commercial Building and Nice Home (Tradtional not contemporary)
Nice to have
• Individual Buttons or links to "Commercial, Residential, Farm/Ranch, Land"
Contact Data displayed
button that says "Maple Crest"-next to button is Maple Crest Logo-see www.maplecrestvale.bz
Links to "Buyers and "Sellers"
Links to Facebook, twitter,.....etc
Should not have
• 20+ story commercial buildings or ultra modern. See uploaded files of typical buildings for commercial.

```html
<!DOCTYPE html>
<html lang="en">
<head>
<meta charset="utf-8">
<title>Properties by Vandel</title>
<link href="https://fonts.googleapis.com/css2?family=Ubuntu:wght@300;400;500&display=swap" rel="stylesheet">
<style>
:root{
  --blue:#2b9fd9;
  --blue-dark:#1f86bd;
  --ink:#1d1d1d;
  --text:#333;
  --muted:#888;
  --line:#c9dde6;
  --panel:#1b1b1b;
  --field:#111;
  --band:#2f2f2f;
  --band-top:#222;
  --grey:#e3e3e3;
  --white:#fff;
}
*{box-sizing:border-box;margin:0;padding:0}
html,body{width:1036px;height:1200px;overflow:hidden}
body{
  position:relative;
  font-family:"Ubuntu",Arial,sans-serif;
  color:var(--text);
  background:
    radial-gradient(ellipse 420px 140px at 518px 470px,#fafafa 0%,rgba(250,250,250,0) 100%),
    linear-gradient(180deg,#fff 0,#fff 260px,#e6e6e6 300px,#ececec 480px,#dcdcdc 800px,#e8e8e8 1200px);
}
.abs{position:absolute}

/* header */
.brand{left:127px;top:0;width:100px;height:52px}
.brand-bar{left:127px;top:0;width:100px;height:4px;background:var(--blue)}
.brand-name{left:127px;top:10px;color:var(--ink);font-weight:400;line-height:1}
.brand-name .small{display:block;font-size:9px;letter-spacing:.5px;text-align:right;width:100px}
.brand-name .big{display:block;font-size:32px;letter-spacing:-1px;margin-top:1px}
.call{left:744px;top:24px;display:flex;align-items:center;gap:12px;font-size:11.5px;color:var(--blue)}
.call .dot{width:21px;height:21px;border-radius:50%;background:var(--blue);display:flex;align-items:center;justify-content:center}
.call .sep{width:1px;height:18px;background:var(--blue);margin:0 2px}
.top-rule{left:128px;top:70px;width:773px;height:1px;background:var(--line)}
.nav-tab{left:167px;top:69px;width:54px;height:2px;background:var(--blue-dark)}
.nav{left:128px;top:83px;width:773px;height:18px;font-size:12px;color:#222}
.nav a{position:absolute;color:inherit;text-decoration:none;transform:translateX(-50%);white-space:nowrap}
.blue-rule{left:128px;top:109px;width:773px;height:5px;background:var(--blue)}

/* hero */
.hero{left:128px;top:114px;width:773px;height:312px;overflow:hidden;background:#fff}
.hero-photo{position:absolute;left:0;top:0;width:773px;height:312px;
  background:linear-gradient(180deg,#8fb7e0 0%,#bcd4ea 30%,#6b5a4d 45%,#3b3a38 70%,#5d6c3a 85%,#8c8a82 100%)}
.hero-panel{position:absolute;inset:0}
.search-title{left:656px;top:143px;width:202px;text-align:center;color:#eee;font-size:15.5px;font-weight:400}
.field{position:absolute;width:96px;height:26px;background:var(--field);border:1px solid #2d2d2d;border-radius:4px;
  box-shadow:inset 0 1px 3px #000;color:#c8c8c8;font-size:8.5px;padding:8px 0 0 7px}
.submit{left:673px;top:364px;width:165px;height:26px;border-radius:6px;background:var(--blue);color:#fff;
  font-size:11.5px;text-align:center;line-height:26px}
.arrow{width:40px;height:43px;background:linear-gradient(180deg,#222,#000);color:#fff;font-size:18px;
  display:flex;align-items:center;justify-content:center;border-radius:2px}
.hero-shadow{left:190px;top:426px;width:650px;height:30px;
  background:radial-gradient(ellipse 50% 60% at 50% 0,rgba(0,0,0,.28),rgba(0,0,0,0))}

/* services */
.card{background:var(--white)}
.services{left:112px;top:481px;width:812px;height:302px}
.service .icon{position:absolute;width:40px;height:40px;border-radius:50%;background:var(--blue);display:flex;align-items:center;justify-content:center}
.service h3{position:absolute;font-weight:400;font-size:15.5px;color:var(--blue);white-space:nowrap}
.service p{position:absolute;width:160px;font-size:10px;line-height:13px;color:#222}
.service .more{position:absolute;font-size:10px;color:var(--blue)}
.divider{left:112px;top:703px;width:812px;height:1px;background:#e2e2e2}
.represent{left:190px;top:725px;font-size:29px;font-weight:400;color:var(--blue)}
.brand-mini{left:748px;top:720px;color:var(--ink);line-height:1}
.brand-mini .small{display:block;font-size:8px;text-align:right;width:98px;letter-spacing:.4px}
.brand-mini .big{display:block;font-size:31px;letter-spacing:-1px}

/* community band */
.band-top{left:112px;top:783px;width:812px;height:18px;background:linear-gradient(180deg,var(--band-top),#2a2a2a);
  clip-path:polygon(0 0,100% 0,100% 100%,0 100%)}
.band{left:112px;top:783px;width:812px;height:77px;background:var(--band);
  box-shadow:0 10px 14px -8px rgba(0,0,0,.35)}
.band-edge{left:112px;top:783px;width:812px;height:16px;background:#1f1f1f;clip-path:polygon(0 0,100% 0,97% 100%,3% 100%)}
.band-title{left:189px;top:822px;font-size:16.5px;color:#f2f2f2;font-weight:300}
.band-mark{left:596px;top:808px;width:75px;height:46px;border-radius:4px;
  background:radial-gradient(ellipse at 55% 45%,#d9883a 0,#b86a26 45%,rgba(47,47,47,0) 75%)}
.band-btn{left:724px;top:818px;width:120px;height:26px;background:var(--blue);color:#fff;font-size:13px;
  text-align:center;line-height:26px}

/* footer */
.footer{left:107px;top:886px;width:817px;height:228px}
.foot-col{position:absolute;font-size:10.5px;color:#222}
.foot-col ul{list-style:none}
.foot-col li{height:19.5px}
.foot-col h4{font-weight:400;font-size:10.5px;margin-bottom:9px}
.post p{font-size:9.8px;line-height:11.5px;width:165px}
.post p a{color:var(--blue);text-decoration:none}
.post time{display:block;font-size:8.5px;color:#555;margin:10px 0 12px}
.input{width:139px;height:18px;background:#e8e8e8;border:1px solid #cfcfcf;border-radius:3px;font-size:8.5px;color:#888;padding:4px 0 0 9px;margin-bottom:4px}
.subscribe{width:139px;height:18px;background:var(--blue);color:#fff;font-size:9px;padding:4px 0 0 9px;border-radius:2px}
.contact li{display:flex;align-items:center;gap:10px;height:22px;font-size:9.8px}
.contact svg{width:13px;height:13px;flex:none}
.bottom{left:107px;top:1134px;width:817px;height:66px}
.socials{left:137px;top:1165px;display:flex;gap:3px}
.socials span{width:17px;height:17px;border-radius:2px}
.copyright{left:600px;top:1167px;width:298px;text-align:right;font-size:8.5px;color:#222}
.side-shade{top:270px;width:112px;height:930px}
</style>
</head>
<body>

<div class="abs side-shade" style="left:0;background:linear-gradient(90deg,#f3f3f3,#dedede)"></div>
<div class="abs side-shade" style="left:924px;background:linear-gradient(270deg,#f3f3f3,#dedede)"></div>

<header>
  <div class="abs brand-bar"></div>
  <div class="abs brand-name" aria-label="Properties by Vandel">
    <span class="small">PROPERTIES BY</span>
    <span class="big">VANDEL</span>
  </div>
  <div class="abs call">
    <span class="dot">
      <svg width="11" height="11" viewBox="0 0 24 24"><path fill="#fff" d="M6.6 10.8a15.1 15.1 0 0 0 6.6 6.6l2.2-2.2c.3-.3.7-.4 1-.2 1.1.4 2.3.6 3.6.6.6 0 1 .4 1 1V20c0 .6-.4 1-1 1A17 17 0 0 1 3 4c0-.6.4-1 1-1h3.5c.6 0 1 .4 1 1 0 1.3.2 2.5.6 3.6.1.3 0 .7-.2 1z"/></svg>
    </span>
    <span class="sep"></span>
    <span>Call us:&nbsp; 530.555.0142</span>
  </div>
  <div class="abs top-rule"></div>
  <div class="abs nav-tab"></div>
  <nav class="abs nav">
    <a href="#" style="left:65px">Home</a>
    <a href="#" style="left:201px">Service Area</a>
    <a href="#" style="left:373px">Meet the Team</a>
    <a href="#" style="left:553px">Expertise</a>
    <a href="#" style="left:695px">Contact</a>
  </nav>
  <div class="abs blue-rule"></div>
</header>

<section class="abs hero">
  <div class="hero-photo" role="img" aria-label="Photo of the stone and iron entrance gate of the Maple Crest community with shrubs and blue sky"></div>
  <svg class="hero-panel" viewBox="0 0 773 312" width="773" height="312">
    <defs>
      <linearGradient id="panelShade" x1="0" y1="0" x2="0" y2="1">
        <stop offset="0" stop-color="#242424"/><stop offset="1" stop-color="#151515"/>
      </linearGradient>
    </defs>
    <polygon points="517,0 773,0 773,312 409,312" fill="url(#panelShade)"/>
  </svg>
</section>
<div class="abs hero-shadow"></div>

<form class="search" aria-label="Search properties">
  <h2 class="abs search-title">Search Properties</h2>
  <div class="field" style="left:656px;top:178px">Property Type</div>
  <div class="field" style="left:760px;top:178px">Location</div>
  <div class="field" style="left:656px;top:215px">Acreage</div>
  <div class="field" style="left:760px;top:215px">Sq FT</div>
  <div class="field" style="left:656px;top:252px">Min. Price</div>
  <div class="field" style="left:760px;top:252px">Max. Price</div>
  <div class="field" style="left:656px;top:289px">Min. Bed/Bath</div>
  <div class="field" style="left:760px;top:289px">Wishlist</div>
  <div class="field" style="left:656px;top:326px">Name</div>
  <div class="field" style="left:760px;top:326px">Email</div>
  <div class="abs submit">Submit</div>
</form>

<div class="abs arrow" style="left:108px;top:253px">&lsaquo;</div>
<div class="abs arrow" style="left:881px;top:253px">&rsaquo;</div>

<section class="abs card services">
  <div class="service">
    <div class="icon" style="left:24px;top:58px">
      <svg width="16" height="16" viewBox="0 0 24 24"><path fill="#fff" d="M12 3 2 12h3v9h5v-6h4v6h5v-9h3z"/></svg>
    </div>
    <h3 style="left:83px;top:68px">Residential</h3>
    <p style="left:24px;top:114px">Whether you are looking for a replacement residence or adream home you're in goodhands with TQV...</p>
    <span class="more" style="left:24px;top:170px">&lt;&lt; More</span>
  </div>
  <div class="service">
    <div class="icon" style="left:222px;top:58px">
      <svg width="16" height="16" viewBox="0 0 24 24"><path fill="#fff" d="M9 4h6v3h5v12H4V7h5zm2 3h2V6h-2z"/></svg>
    </div>
    <h3 style="left:281px;top:68px">Commercial</h3>
    <p style="left:222px;top:114px">TQV knows the current market and the local inventory. Our experts know what affects valueand your ROI...</p>
    <span class="more" style="left:222px;top:170px">&lt;&lt; More</span>
  </div>
  <div class="service">
    <div class="icon" style="left:422px;top:58px">
      <svg width="18" height="18" viewBox="0 0 24 24"><path fill="#fff" d="M3 10 12 4l9 6v10H3zm5 4v6h8v-6z"/></svg>
    </div>
    <h3 style="left:481px;top:68px">Farm</h3>
    <p style="left:422px;top:114px">Whether it's bovine, equineor just split-rail and barbed wireTQV will find you what you're hankering for ...</p>
    <span class="more" style="left:422px;top:170px">&lt;&lt; More</span>
  </div>
  <div class="service">
    <div class="icon" style="left:620px;top:58px">
      <svg width="18" height="18" viewBox="0 0 24 24"><circle cx="12" cy="8" r="3.5" fill="#fff"/><path fill="#fff" d="M2 19c4-5 7-6 10-4s5 1 10-2v6z"/></svg>
    </div>
    <h3 style="left:679px;top:68px">Land</h3>
    <p style="left:620px;top:114px">We have lake views, river views, mountain views,meadow views, valley views,and views of rolling oaks...</p>
    <span class="more" style="left:620px;top:170px">&lt;&lt; More</span>
  </div>
</section>
<div class="abs divider"></div>
<h2 class="abs represent">Buyer &amp; Seller Representation</h2>
<div class="abs brand-mini" aria-label="Properties by Vandel">
  <span class="small">PROPERTIES BY</span>
  <span class="big">VANDEL</span>
</div>

<section class="community">
  <div class="abs band"></div>
  <div class="abs band-edge"></div>
  <p class="abs band-title">MAPLE CREST Gated Equestrian Community</p>
  <div class="abs band-mark" role="img" aria-label="Maple Crest community emblem"></div>
  <a class="abs band-btn">Maple Crest</a>
</section>

<footer>
  <div class="abs card footer">
    <div class="foot-col" style="left:27px;top:60px">
      <ul><li>About</li><li>Services</li><li>Residential</li><li>Land</li><li>Commercial</li></ul>
    </div>
    <div class="foot-col" style="left:129px;top:60px">
      <ul><li>Privacy</li><li>Terms</li></ul>
    </div>
    <div class="foot-col post" style="left:224px;top:60px">
      <h4>Latest Post</h4>
      <p>Lorem ipsdum dolor sit amet this is a sample blog post lorem ipsum dolor sit amet <a>&lt;&lt;more</a></p>
      <time>8/9/2013</time>
      <p>Lorem ipsdum dolor sit amet this is a sample blog post lorem ipsum dolor sit amet <a>&lt;&lt;more</a></p>
      <time>8/9/2013</time>
    </div>
    <div class="foot-col" style="left:423px;top:60px">
      <h4>Get Property Alerts</h4>
      <div class="input">Name</div>
      <div class="input">Email</div>
      <div class="subscribe">Subscribe</div>
    </div>
    <div class="foot-col contact" style="left:642px;top:60px">
      <h4>Contact</h4>
      <ul>
        <li><svg viewBox="0 0 24 24"><path fill="#333" d="M12 3 2 12h3v9h5v-6h4v6h5v-9h3z"/></svg>Address, TQ Vandel</li>
        <li><svg viewBox="0 0 24 24"><path fill="#333" d="M6.6 10.8a15.1 15.1 0 0 0 6.6 6.6l2.2-2.2c.3-.3.7-.4 1-.2 1.1.4 2.3.6 3.6.6.6 0 1 .4 1 1V20c0 .6-.4 1-1 1A17 17 0 0 1 3 4c0-.6.4-1 1-1h3.5c.6 0 1 .4 1 1 0 1.3.2 2.5.6 3.6.1.3 0 .7-.2 1z"/></svg>530.555.0142</li>
        <li><svg viewBox="0 0 24 24"><rect x="3" y="5" width="18" height="14" rx="1" fill="none" stroke="#333" stroke-width="2"/><path d="m3 6 9 7 9-7" fill="none" stroke="#333" stroke-width="2"/></svg>info@tqvandel.com</li>
      </ul>
    </div>
  </div>
  <div class="abs card bottom"></div>
  <div class="abs socials" aria-label="Social links">
    <span style="background:#3b5998"></span>
    <span style="background:#2fa6dd"></span>
    <span style="background:#c8232c"></span>
    <span style="background:#0e76a8"></span>
    <span style="background:#d9352a"></span>
  </div>
  <p class="abs copyright">Copyright @ 2014 TQ Vandel. All Right Reserved</p>
</footer>

</body>
</html>
```